Corvane semiconductor corporate presentation

We need a new template with some fresh design elements as we've just announced the acquisition of a new company. Similarly, the backend of the ppt is not set up correctly - and doesn't format properly when dropping in copied text. Attached is the powerpoint presentation/ template as it stands today.
Industry/Entity Type
It Company
Font styles to use
Other font styles liked:
- Arial
Look and feel
Each slider illustrates characteristics of the customer's brand and the style your logo design should communicate.

```html
<!DOCTYPE html>
<html lang="en">
<head>
<meta charset="utf-8">
<title>Corvane semiconductor – Corporate Presentation</title>
<link href="https://fonts.googleapis.com/css2?family=Open+Sans:wght@400;600;700&display=swap" rel="stylesheet">
<style>
:root{
  --canvas:#8c8c8c;
  --teal:#1aaecb;
  --teal-dark:#0b6f8c;
  --teal-light:#bfe9f2;
  --ink:#4a4a4a;
  --muted:#9a9a9a;
  --purple:#6a3d8f;
  --blue:#1d5fa8;
  --white:#ffffff;
}
*{margin:0;padding:0;box-sizing:border-box}
html,body{width:723px;height:1200px;overflow:hidden;background:var(--canvas);font-family:"Open Sans",Arial,sans-serif}
.deck{position:relative;width:723px;height:1200px}
.slide{position:absolute;width:182px;height:90px;background:var(--white);overflow:hidden;box-shadow:0 1px 2px rgba(0,0,0,.25)}
.abs{position:absolute}
.heading{position:absolute;left:8px;top:6px;font-size:5px;font-weight:700;color:var(--teal)}
.copy{font-size:3px;line-height:1.35;color:var(--ink)}
.copy-white{font-size:3px;line-height:1.35;color:var(--white)}
.photo{position:absolute}
.tealbox{position:absolute;background:var(--teal)}
.dot{display:inline-block;width:4px;height:4px;border-radius:50%;background:var(--teal);vertical-align:middle;margin-right:3px}
.icon-tile{position:absolute;width:18px;height:14px;background:var(--teal);border-radius:1px}
.icon-tile::after{content:"";position:absolute;left:6px;top:4px;width:6px;height:6px;border:1px solid #fff;border-radius:50%}
.caption{position:absolute;font-size:2.6px;color:var(--ink);text-align:center}
table.data{position:absolute;border-collapse:collapse;font-size:2.6px;color:var(--ink)}
table.data th{background:var(--teal);color:#fff;font-weight:600;padding:1px 2px;text-align:left}
table.data td{padding:1px 2px;border-bottom:.5px solid #dde}
table.data tr:nth-child(even) td{background:#eef8fb}
.brand{position:absolute;color:#fff;font-weight:700;font-size:7px;display:flex;align-items:center;gap:2px}
.brand i{width:5px;height:5px;border-radius:50%;background:#fff;display:block}
</style>
</head>
<body>
<div class="deck">

<!-- Row 1 -->
<section class="slide" style="left:68px;top:28px">
  <div class="photo" role="img" aria-label="Dark teal technology backdrop" style="inset:0;background:linear-gradient(120deg,#0a3f57,#127d9c 55%,#1aaecb)"></div>
  <div class="brand" style="left:8px;top:8px"><i></i>Corvane</div>
  <div class="abs" style="left:60px;top:44px;color:#fff;font-size:7px;font-weight:600">Corporate Presentation</div>
  <div class="abs copy-white" style="left:100px;top:54px">Month Year</div>
</section>

<section class="slide" style="left:271px;top:28px">
  <div class="heading">Agenda</div>
  <div class="abs copy" style="left:10px;top:26px"><span class="dot"></span>Company overview</div>
  <div class="abs copy" style="left:10px;top:40px"><span class="dot"></span>Our products</div>
  <div class="abs copy" style="left:10px;top:54px"><span class="dot"></span>Results and outlook</div>
  <div class="photo" role="img" aria-label="Two colleagues looking at a screen" style="left:88px;top:0;width:94px;height:90px;background:linear-gradient(135deg,#c9c5bd,#6f7479)"></div>
</section>

<section class="slide" style="left:474px;top:28px">
  <div class="heading">About us</div>
  <div class="photo" role="img" aria-label="Office building facade" style="left:60px;top:14px;width:116px;height:42px;background:linear-gradient(135deg,#dfe6ea,#8fa3ad)"></div>
  <div class="abs copy" style="left:8px;top:62px;width:166px">Short overview text about the company and its focus areas goes here.</div>
</section>

<!-- Row 2 -->
<section class="slide" style="left:68px;top:132px">
  <div class="heading">Key facts</div>
  <div class="icon-tile" style="left:12px;top:22px"></div><div class="icon-tile" style="left:54px;top:22px"></div>
  <div class="icon-tile" style="left:96px;top:22px"></div><div class="icon-tile" style="left:138px;top:22px"></div>
  <div class="icon-tile" style="left:12px;top:56px"></div><div class="icon-tile" style="left:54px;top:56px"></div>
  <div class="icon-tile" style="left:96px;top:56px"></div><div class="icon-tile" style="left:138px;top:56px"></div>
</section>

<section class="slide" style="left:271px;top:132px">
  <div class="heading">Leadership</div>
  <svg class="abs" style="left:8px;top:16px" width="166" height="70" role="img" aria-label="Grid of team member portraits">
    <g fill="#9fb4bd">
      <rect x="0" y="0" width="24" height="24"/><rect x="28" y="0" width="24" height="24"/><rect x="56" y="0" width="24" height="24"/><rect x="84" y="0" width="24" height="24"/><rect x="112" y="0" width="24" height="24"/><rect x="140" y="0" width="24" height="24"/>
      <rect x="0" y="36" width="24" height="24"/><rect x="28" y="36" width="24" height="24"/><rect x="56" y="36" width="24" height="24"/><rect x="84" y="36" width="24" height="24"/><rect x="112" y="36" width="24" height="24"/><rect x="140" y="36" width="24" height="24"/>
    </g>
    <g fill="#1aaecb">
      <rect x="0" y="24" width="24" height="5"/><rect x="28" y="24" width="24" height="5"/><rect x="56" y="24" width="24" height="5"/><rect x="84" y="24" width="24" height="5"/><rect x="112" y="24" width="24" height="5"/><rect x="140" y="24" width="24" height="5"/>
      <rect x="0" y="60" width="24" height="5"/><rect x="28" y="60" width="24" height="5"/><rect x="56" y="60" width="24" height="5"/><rect x="84" y="60" width="24" height="5"/><rect x="112" y="60" width="24" height="5"/><rect x="140" y="60" width="24" height="5"/>
    </g>
  </svg>
</section>

<section class="slide" style="left:474px;top:132px">
  <div class="heading">Our values</div>
  <div class="icon-tile" style="left:16px;top:20px"></div><div class="icon-tile" style="left:60px;top:20px"></div>
  <div class="icon-tile" style="left:104px;top:20px"></div><div class="icon-tile" style="left:148px;top:20px"></div>
  <div class="icon-tile" style="left:16px;top:54px"></div><div class="icon-tile" style="left:60px;top:54px"></div>
  <div class="icon-tile" style="left:104px;top:54px"></div><div class="icon-tile" style="left:148px;top:54px"></div>
  <div class="caption" style="left:8px;top:37px;width:170px">Value one · Value two · Value three · Value four</div>
</section>

<!-- Row 3 -->
<section class="slide" style="left:68px;top:236px">
  <div class="heading">Divisions</div>
  <div class="abs" style="left:10px;top:18px;width:50px;height:28px;background:var(--purple)"></div>
  <div class="abs" style="left:66px;top:18px;width:50px;height:28px;background:var(--teal)"></div>
  <div class="abs" style="left:122px;top:18px;width:50px;height:28px;background:var(--blue)"></div>
  <div class="abs copy" style="left:10px;top:52px;width:50px">Division text</div>
  <div class="abs copy" style="left:66px;top:52px;width:50px">Division text</div>
  <div class="abs copy" style="left:122px;top:52px;width:50px">Division text</div>
</section>

<section class="slide" style="left:271px;top:236px">
  <div class="heading">Markets</div>
  <svg class="abs" style="left:10px;top:20px" width="162" height="60">
    <g fill="none" stroke="#1aaecb" stroke-width="1.2">
      <circle cx="12" cy="8" r="5"/><circle cx="58" cy="8" r="5"/><circle cx="104" cy="8" r="5"/><circle cx="150" cy="8" r="5"/>
      <circle cx="12" cy="38" r="5"/><circle cx="58" cy="38" r="5"/><circle cx="104" cy="38" r="5"/><circle cx="150" cy="38" r="5"/>
    </g>
  </svg>
  <div class="caption" style="left:8px;top:34px;width:166px">Mobile · Automotive · Industrial · Connectivity</div>
  <div class="caption" style="left:8px;top:64px;width:166px">Power · Audio · Sensors · Wireless</div>
</section>

<section class="slide" style="left:474px;top:236px">
  <div class="heading">Global reach</div>
  <div class="abs copy" style="left:8px;top:20px;width:64px">Offices and design centres across the globe.</div>
  <div class="photo" role="img" aria-label="City skyline by the water" style="left:80px;top:14px;width:96px;height:64px;background:linear-gradient(180deg,#9cc6dd,#3f6f8d)"></div>
</section>

<!-- Row 4 -->
<section class="slide" style="left:68px;top:340px">
  <div class="heading">Capabilities</div>
  <div class="tealbox" style="left:0;top:28px;width:182px;height:40px"></div>
  <div class="abs" style="left:24px;top:36px;width:22px;height:22px;background:#fff"></div>
  <div class="abs" style="left:62px;top:36px;width:22px;height:22px;background:#fff"></div>
  <div class="abs" style="left:100px;top:36px;width:22px;height:22px;background:#fff"></div>
  <div class="abs" style="left:138px;top:36px;width:22px;height:22px;background:#fff"></div>
</section>

<section class="slide" style="left:271px;top:340px">
  <div class="heading">Meet the team</div>
  <div class="photo" role="img" aria-label="Round portrait" style="left:34px;top:18px;width:26px;height:26px;border-radius:50%;background:#8eb2c0;border:1.5px solid var(--teal)"></div>
  <div class="photo" role="img" aria-label="Round portrait" style="left:78px;top:18px;width:26px;height:26px;border-radius:50%;background:#8eb2c0;border:1.5px solid var(--teal)"></div>
  <div class="photo" role="img" aria-label="Round portrait" style="left:122px;top:18px;width:26px;height:26px;border-radius:50%;background:#8eb2c0;border:1.5px solid var(--teal)"></div>
  <div class="caption" style="left:26px;top:50px;width:130px">Name · Name · Name</div>
  <div class="caption" style="left:26px;top:56px;width:130px">Job title · Job title · Job title</div>
</section>

<section class="slide" style="left:474px;top:340px">
  <div class="tealbox" style="left:0;top:0;width:90px;height:90px"></div>
  <div class="abs" style="left:8px;top:30px;color:#fff;font-size:5px;font-weight:700">Our strategy</div>
  <div class="abs copy-white" style="left:8px;top:40px;width:74px">Short statement about direction.</div>
  <div class="photo" role="img" aria-label="Person using a smartwatch" style="left:90px;top:0;width:92px;height:90px;background:linear-gradient(135deg,#d8cbbd,#7d8a8f)"></div>
</section>

<!-- Row 5 -->
<section class="slide" style="left:68px;top:444px">
  <div class="heading">Process</div>
  <svg class="abs" style="left:8px;top:16px" width="80" height="70">
    <g fill="#1aaecb"><rect x="0" y="0" width="40" height="10"/><rect x="0" y="20" width="40" height="10"/><rect x="0" y="40" width="40" height="10"/><rect x="0" y="60" width="40" height="10"/></g>
    <g stroke="#1aaecb" stroke-width="1"><line x1="40" y1="5" x2="60" y2="5"/><line x1="40" y1="25" x2="60" y2="25"/><line x1="40" y1="45" x2="60" y2="45"/><line x1="40" y1="65" x2="60" y2="65"/></g>
    <g fill="#1aaecb"><circle cx="63" cy="5" r="3"/><circle cx="63" cy="25" r="3"/><circle cx="63" cy="45" r="3"/><circle cx="63" cy="65" r="3"/></g>
  </svg>
  <div class="abs copy" style="left:80px;top:19px">Step one details</div>
  <div class="abs copy" style="left:80px;top:39px">Step two details</div>
  <div class="abs copy" style="left:80px;top:59px">Step three details</div>
  <div class="abs copy" style="left:80px;top:79px">Step four details</div>
</section>

<section class="slide" style="left:271px;top:444px">
  <div class="photo" role="img" aria-label="Woman holding a phone" style="left:0;top:0;width:84px;height:90px;background:linear-gradient(135deg,#e6d8c8,#8fa4ad)"></div>
  <div class="tealbox" style="left:96px;top:24px;width:76px;height:40px"></div>
  <div class="abs copy-white" style="left:100px;top:30px;width:68px">Customer focus message goes here.</div>
</section>

<section class="slide" style="left:474px;top:444px">
  <div class="heading">Applications</div>
  <div class="photo" role="img" aria-label="Product photo" style="left:8px;top:18px;width:38px;height:34px;background:#8aa3ad"></div>
  <div class="photo" role="img" aria-label="Product photo" style="left:50px;top:18px;width:38px;height:34px;background:#a49a8e"></div>
  <div class="photo" role="img" aria-label="Product photo" style="left:92px;top:18px;width:38px;height:34px;background:#7e96a3"></div>
  <div class="photo" role="img" aria-label="Product photo" style="left:134px;top:18px;width:38px;height:34px;background:#9aa9a0"></div>
  <div class="tealbox" style="left:8px;top:54px;width:38px;height:16px"></div><div class="tealbox" style="left:50px;top:54px;width:38px;height:16px"></div>
  <div class="tealbox" style="left:92px;top:54px;width:38px;height:16px"></div><div class="tealbox" style="left:134px;top:54px;width:38px;height:16px"></div>
</section>

<!-- Row 6 -->
<section class="slide" style="left:68px;top:548px">
  <div class="photo" role="img" aria-label="Car dashboard interior" style="left:0;top:0;width:78px;height:90px;background:linear-gradient(135deg,#3c4a52,#9aa8ae)"></div>
  <div class="abs" style="left:86px;top:14px;font-size:5px;font-weight:700;color:var(--teal)">Automotive</div>
  <div class="abs copy" style="left:86px;top:24px;width:88px">Body text describing this market and our role in it for partners.</div>
</section>

<section class="slide" style="left:271px;top:548px">
  <div class="heading">Milestones</div>
  <svg class="abs" style="left:10px;top:22px" width="162" height="40">
    <line x1="8" y1="14" x2="154" y2="14" stroke="#1aaecb" stroke-width="1"/>
    <g fill="#fff" stroke="#1aaecb" stroke-width="1.2"><circle cx="12" cy="14" r="8"/><circle cx="46" cy="14" r="8"/><circle cx="80" cy="14" r="8"/><circle cx="114" cy="14" r="8"/><circle cx="148" cy="14" r="8"/></g>
  </svg>
  <div class="caption" style="left:10px;top:60px;width:162px">2016 · 2018 · 2020 · 2022 · 2024</div>
</section>

<section class="slide" style="left:474px;top:548px">
  <div class="heading">Highlights</div>
  <div class="tealbox" style="left:8px;top:22px;width:16px;height:10px"></div><div class="abs copy" style="left:28px;top:24px">Highlight one</div>
  <div class="tealbox" style="left:8px;top:38px;width:16px;height:10px"></div><div class="abs copy" style="left:28px;top:40px">Highlight two</div>
  <div class="tealbox" style="left:8px;top:54px;width:16px;height:10px"></div><div class="abs copy" style="left:28px;top:56px">Highlight three</div>
  <div class="photo" role="img" aria-label="Close-up of a device" style="left:90px;top:14px;width:86px;height:66px;background:linear-gradient(135deg,#c0553f,#6a7b85)"></div>
</section>

<!-- Row 7 -->
<section class="slide" style="left:68px;top:652px">
  <div class="heading">Innovation</div>
  <div class="photo" role="img" aria-label="Plant and laboratory scene" style="left:8px;top:16px;width:60px;height:40px;background:linear-gradient(135deg,#8fb08a,#3f6b6f)"></div>
  <div class="abs copy" style="left:74px;top:18px;width:100px">Text about research and development investment across sites.</div>
  <div class="tealbox" style="left:74px;top:52px;width:100px;height:28px"></div>
</section>

<section class="slide" style="left:271px;top:652px">
  <div class="heading">Sustainability</div>
  <div class="abs copy" style="left:8px;top:18px;width:66px">Longer body copy about our sustainability goals and yearly progress.</div>
  <div class="photo" role="img" aria-label="City landscape" style="left:80px;top:10px;width:94px;height:38px;background:linear-gradient(135deg,#8fb3c9,#466b7e)"></div>
  <div class="photo" role="img" aria-label="Aerial view of fields" style="left:80px;top:50px;width:46px;height:32px;background:#7d9a6f"></div>
  <div class="photo" role="img" aria-label="Coastline" style="left:128px;top:50px;width:46px;height:32px;background:#6b93a8"></div>
</section>

<section class="slide" style="left:474px;top:652px">
  <div class="heading">Revenue split</div>
  <div class="abs copy" style="left:8px;top:20px;width:80px">Revenue by segment for the last fiscal year.</div>
  <svg class="abs" style="left:100px;top:14px" width="64" height="64" viewBox="0 0 64 64">
    <circle cx="32" cy="32" r="30" fill="#1aaecb"/>
    <path d="M32 32 L32 2 A30 30 0 0 1 60 42 Z" fill="#0b6f8c"/>
    <path d="M32 32 L60 42 A30 30 0 0 1 20 60 Z" fill="#7fd3e4"/>
    <path d="M32 32 L20 60 A30 30 0 0 1 3 26 Z" fill="#bfe9f2"/>
  </svg>
</section>

<!-- Row 8 -->
<section class="slide" style="left:68px;top:756px">
  <div class="heading">Financials</div>
  <table class="data" style="left:8px;top:16px;width:166px">
    <tr><th>Item</th><th>2022</th><th>2023</th><th>2024</th></tr>
    <tr><td>Revenue</td><td>00</td><td>00</td><td>00</td></tr>
    <tr><td>Margin</td><td>00</td><td>00</td><td>00</td></tr>
    <tr><td>Profit</td><td>00</td><td>00</td><td>00</td></tr>
    <tr><td>Cash</td><td>00</td><td>00</td><td>00</td></tr>
    <tr><td>Staff</td><td>00</td><td>00</td><td>00</td></tr>
  </table>
</section>

<section class="slide" style="left:271px;top:756px">
  <div class="heading">Acquisition</div>
  <div class="photo" role="img" aria-label="Panoramic aurora landscape" style="left:8px;top:16px;width:166px;height:30px;background:linear-gradient(90deg,#2e4b5c,#3e8f8a,#5a3f6e)"></div>
  <div class="tealbox" style="left:8px;top:52px;width:38px;height:26px"></div><div class="tealbox" style="left:50px;top:52px;width:38px;height:26px"></div>
  <div class="tealbox" style="left:92px;top:52px;width:38px;height:26px"></div><div class="tealbox" style="left:134px;top:52px;width:38px;height:26px"></div>
</section>

<section class="slide" style="left:474px;top:756px">
  <div class="heading">Summary</div>
  <table class="data" style="left:20px;top:20px;width:142px">
    <tr><th>Metric</th><th>Value</th><th>Change</th></tr>
    <tr><td>Metric one</td><td>00</td><td>+0%</td></tr>
    <tr><td>Metric two</td><td>00</td><td>+0%</td></tr>
    <tr><td>Metric three</td><td>00</td><td>+0%</td></tr>
    <tr><td>Metric four</td><td>00</td><td>+0%</td></tr>
  </table>
</section>

<!-- Row 9 -->
<section class="slide" style="left:271px;top:860px">
  <div class="photo" role="img" aria-label="Blurred office background" style="inset:0;background:linear-gradient(135deg,#d5dbde,#7b878c)"></div>
  <div class="tealbox" style="left:16px;top:40px;width:40px;height:40px"></div>
  <div class="abs" style="left:20px;top:54px;color:#fff;font-size:5px;font-weight:700">Thank you</div>
</section>

</div>
</body>
</html>
```